WP website design Hallek

We need a wordpress design that will incorporate a professional color scheme with company logo in a clean layout. The design needs to consider that this will be developed on a responsive theme. Colors are green of the logo, and tan and an accent color maybe black. Client wants a 'modern' look.

Industry/Entity Type

It Company

Font styles to use
Serif
Sans Serif

Colors

Requirements
Must have
• Must Have:
- Navigation: 1) Home; 2) Auctions; 3) Real Estate Listings 4) Mortgage Tips 5) Buying & Selling Tips 6) Sell A Farm 7) About Us 8) Contact Us

Site will have slideshow - image is attached. Colors will be those in the logo, tan and an accent color, maybe black.

Widgets: Featured Auctions, 2) Email signup form; 3) Testimonials widget; 4) Featured Properties; 5) Social Media (ZN, crewLoop, RSS); 6) News & Events. Footer will have affiliation logo and contact info.

Home page content:
We are a family owned and operated business with over 25 years of real estate experience in Clinton and surrounding areas in Western Oklahoma. We know that purchasing a home is one of the most important decisions a person can make, and we strive to make it a successful and enjoyable experience for you!
Enjoy our website and please call if you have any questions or would like to make an appointment to view property!
Also, take a moment to look at our Auction Calendar for upcoming auction dates. Auctions are a great opportunity for great deals and rare finds, not to mention A LOT OF FUN!!

Widgets: 1) Featured Properties; 2) Call to action for Sellers 3) Testimonials blog/widget
Nice to have
• use of dropdown menus styling displayed - 1) Current Auctions & 2) Past Auctions under the Auctions link

```html
<!DOCTYPE html>
<html lang="en">
<head>
<meta charset="utf-8">
<title>Hallek Real Estate &amp; Auction Co.</title>
<link href="https://fonts.googleapis.com/css2?family=Libre+Baskerville&family=Open+Sans:ital,wght@0,400;0,600;0,700;1,400;1,700&family=Arimo:ital,wght@0,400;0,700;1,400;1,700&display=swap" rel="stylesheet">
<style>
:root{
  --green:#0b4d12;
  --tan:#d3b68b;
  --beige:#cfc59a;
  --panel:#efefef;
  --border:#bdbdbd;
  --ink:#1f1f1f;
  --black:#161616;
  --red:#c0142a;
  --maroon:#8a1020;
  --white:#ffffff;
}
*{margin:0;padding:0;box-sizing:border-box}
html,body{width:847px;height:1200px;overflow:hidden}
body{position:relative;background:var(--tan);font-family:'Arimo',Arial,sans-serif;color:var(--ink)}

.main-nav{position:absolute;left:0;top:0;width:847px;height:38px;background:var(--green)}
.main-nav a{position:absolute;top:12px;font-size:10.5px;color:var(--white);text-decoration:none;white-space:nowrap}
.dropdown{position:absolute;left:133px;top:36px;width:113px;height:54px;background:var(--black);border-radius:2px}
.dropdown::before{content:"";position:absolute;left:21px;top:-5px;border:5px solid transparent;border-top:0;border-bottom-color:var(--black)}
.dropdown a{display:block;height:24px;line-height:24px;padding-left:10px;font-size:10.5px;color:var(--white);text-decoration:none;margin-top:3px}
.dropdown a.active{background:var(--green);margin-top:0}

.page{position:absolute;left:71px;top:64px;width:706px;height:1005px;background:var(--white)}

.brand-panel{position:absolute;left:77px;top:69px;width:257px;height:264px;background:var(--beige)}
.wordmark{position:absolute;display:flex;align-items:center;gap:10px;font-family:'Open Sans',sans-serif;font-weight:600;white-space:nowrap}
.wordmark .mark{display:block;background:currentColor}
.header-mark{left:100px;top:100px;font-size:36px;color:var(--green)}
.header-mark .mark{width:14px;height:14px}
.footer-mark{left:596px;top:50px;font-size:30px;color:var(--white)}
.footer-mark .mark{width:12px;height:12px}

.signup{position:absolute;left:90px;top:182px;width:232px;height:137px;background:var(--green);color:var(--white)}
.signup h3{position:absolute;left:12px;top:4px;font-family:'Libre Baskerville',Georgia,serif;font-weight:400;font-size:19px}
.signup p{position:absolute;left:14px;top:33px;width:200px;font-family:'Open Sans',sans-serif;font-size:10px;line-height:14px}
.signup .email{position:absolute;left:14px;top:76px;width:127px;height:24px;background:var(--white);color:#888;font-size:9.5px;line-height:24px;padding-left:8px}
.signup .btn{position:absolute;left:141px;top:76px;width:71px;height:24px;background:linear-gradient(#d9ad76,#b98a50);color:var(--black);font-family:'Open Sans',sans-serif;font-weight:700;font-size:12px;line-height:24px;text-align:center;border-radius:0 3px 3px 0}

.hero{position:absolute;left:334px;top:69px;width:439px;height:264px;background:linear-gradient(180deg,#a9bfd6 0%,#b07060 35%,#8a4034 70%,#6a6a66 100%)}

.welcome-title{position:absolute;left:85px;top:359px;font-family:'Open Sans',sans-serif;font-weight:700;font-size:15.5px;color:var(--green);letter-spacing:.2px}
.welcome p{position:absolute;left:86px;width:424px;font-size:11px;line-height:14.2px;color:var(--ink)}

.cta{position:absolute;left:545px;top:341px;width:223px;height:43px;background:var(--green);border-radius:3px;color:var(--white);font-family:'Open Sans',sans-serif;font-weight:700;font-size:19.5px;line-height:43px;text-align:center}

.widget{position:absolute;background:var(--panel);border:1px solid var(--border)}
.widget h2{font-family:'Libre Baskerville',Georgia,serif;font-weight:400;font-size:19px;color:var(--ink);position:absolute;left:15px}
.widget .t{position:absolute;font-size:8.6px;color:var(--ink);line-height:11px}
.photo{position:absolute}

.auction{position:absolute;left:85px;width:435px;height:198px;background:var(--panel)}
.auction .photo{left:9px;top:13px;width:161px;height:134px;background:linear-gradient(180deg,#4d86c9 0%,#a8c6e6 35%,#e2d7c8 55%,#8c8a80 85%,#6d8a4a 100%)}
.auction .btn{position:absolute;top:160px;height:20px;color:var(--white);font-size:11px;line-height:20px}
.auction .details{left:9px;width:69px;background:var(--black)}
.auction .gallery{left:94px;width:76px;background:var(--green)}
.auction .btn svg{position:absolute;left:6px;top:4px}
.auction .btn span{position:absolute;left:24px}
.card{position:absolute;left:181px;width:244px;background:var(--white);border:1px solid #dcdcdc;border-radius:3px}
.card .h{position:absolute;left:7px;font-size:11px;color:var(--green)}
.card .s{position:absolute;left:7px;font-size:8.8px;line-height:12px;width:232px;color:var(--ink)}
.auction.alt .card .h{color:var(--red)}

.footer{position:absolute;left:0;top:1056px;width:847px;height:120px;background:var(--green)}
.footer address{position:absolute;left:77px;top:40px;font-style:normal;font-size:9.8px;line-height:12.7px;color:var(--white)}
.copyright{position:absolute;left:0;top:1176px;width:847px;height:24px;background:var(--black);color:var(--white);font-size:10px;line-height:24px;text-align:center}
</style>
</head>
<body>

<nav class="main-nav">
  <a style="left:83px">Home</a>
  <a style="left:140px">Auctions</a>
  <a style="left:209px">Real Estate Listings</a>
  <a style="left:326px">Mortgage Tips</a>
  <a style="left:419px">Buying &amp; Selling Tips</a>
  <a style="left:542px">Sell A Farm</a>
  <a style="left:622px">About Us</a>
  <a style="left:694px">Contact Us</a>
</nav>

<div class="page"></div>

<div class="brand-panel"></div>
<div class="wordmark header-mark"><span class="mark"></span>Hallek</div>

<div class="dropdown">
  <a>Current Auctions</a>
  <a class="active">Past Auctions</a>
</div>

<section class="signup">
  <h3>Email Signup</h3>
  <p>Please join our free mailing list to get auction alerts for upcoming events.</p>
  <div class="email">Enter Your Email</div>
  <div class="btn">Sign Up</div>
</section>

<div class="hero" role="img" aria-label="Slideshow photo of the company's brick storefront with green awnings"></div>

<h1 class="welcome-title">WELCOME TO HALLEK REAL ESTATE</h1>
<div class="welcome">
  <p style="top:391px">We are a family owned and operated business with over 25 years of real estate experience in Clinton and surrounding areas in Western Oklahoma. We know that purchasing a home is one of the most important decisions a person can make, and we strive to make it a successful and enjoyable experience for you!</p>
  <p style="top:462px">Enjoy our website and please call if you have any questions or would like to make an appointment to view property!</p>
  <p style="top:505px">Also, take a moment to look at our Auction Calendar for upcoming auction dates. Auctions are a great opportunity for great deals and rare finds, not to mention A LOT OF FUN!!</p>
</div>

<div class="cta">Seller your Property</div>

<aside class="widget" style="left:550px;top:402px;width:216px;height:215px">
  <h2 style="top:13px">Featured Auctions</h2>
  <div class="t" style="left:0;top:50px;width:214px;text-align:center;font-weight:700">13.35 ACRES OF PRIME DEVELOP<br>&amp; 33RD STREET</div>
  <div class="photo" role="img" aria-label="Photo of a crowd gathered at a house auction" style="left:47px;top:82px;width:126px;height:68px;border:2px solid var(--green);background:linear-gradient(180deg,#9bb8d6 0%,#d9dde0 40%,#6f8b55 100%)"></div>
  <div class="t" style="left:0;top:162px;width:214px;text-align:center">LOTS 13 &amp; 14 FOR SALE, EASTFIELD<br>IOWA<br>Third Street, Eastfield, IA 52600</div>
</aside>

<aside class="widget" style="left:551px;top:631px;width:217px;height:191px">
  <h2 style="top:10px">Featured Auctions</h2>
  <div class="t" style="left:15px;top:40px;font-size:9.5px;font-weight:700">Multi Estate &amp; Consignment Auction</div>
  <div class="photo" role="img" aria-label="Photo of auction attendees in front of a green-roofed house" style="left:14px;top:55px;width:173px;height:69px;background:linear-gradient(180deg,#b9cfe4 0%,#3f9a86 35%,#e6e2d6 55%,#4a4d4a 100%)"></div>
  <div class="t" style="left:15px;top:133px;width:170px"><b>Start Date/ Time:</b> Saturday, April 13, 2013 At 10:00 Am</div>
  <div class="t" style="left:15px;top:163px"><b>Location:</b> 2410 Old Meadow, 73800</div>
</aside>

<aside class="widget" style="left:551px;top:842px;width:217px;height:166px">
  <h2 style="top:14px;font-family:'Open Sans',sans-serif;font-weight:600;font-size:17px">Testimonials Blog</h2>
  <div class="t" style="left:15px;top:54px;width:182px;font-style:italic;font-size:9.2px;line-height:14px"><span style="color:#aaa;font-size:13px">&ldquo;</span> It is a long established fact that a reader will be distracted by the readable content of a page when looking at its layout. The point of using Lorem Ipsum is that it has a more-.. <span style="color:#aaa;font-size:13px">&rdquo;</span></div>
  <div class="t" style="left:15px;top:134px;font-size:9.8px;font-weight:700;font-style:italic;color:var(--maroon)">Carla Denton</div>
</aside>

<article class="auction" style="top:567px">
  <div class="photo" role="img" aria-label="Photo of a two-storey house with a garage"></div>
  <div class="btn details"><svg width="12" height="12" viewBox="0 0 12 12"><circle cx="5" cy="5" r="3.5" fill="none" stroke="#fff" stroke-width="1.6"/><path d="M7.6 7.6 11 11" stroke="#fff" stroke-width="1.8"/></svg><span>Details</span></div>
  <div class="btn gallery"><svg width="14" height="12" viewBox="0 0 14 12"><rect x="1" y="1" width="9" height="7" fill="none" stroke="#fff" stroke-width="1.4"/><rect x="4" y="4" width="9" height="7" fill="#0b4d12" stroke="#fff" stroke-width="1.4"/></svg><span>Gallery</span></div>
  <div class="card" style="top:11px;height:65px">
    <div class="h" style="top:9px">Auction 1</div>
    <div class="s" style="top:28px">Lorem Ipsum is simply dummy text of the printing and typesetting industry.</div>
  </div>
  <div class="card" style="top:90px;height:100px">
    <div class="h" style="top:7px">Online Bidding Only</div>
    <div class="s" style="top:23px">Began:&nbsp; Friday, May 24, 2013 at 10:06 AM EDT</div>
    <div class="s" style="top:43px"><b>Location</b><br>1720 Birch Ln. NW Ridgeview, IA 52400</div>
    <div class="s" style="top:69px;font-size:9.6px">Field tractor w/Hartline Loader, Dune Cutditioner: SHOP &amp; MISCELLANIOUS &amp; PORK .</div>
  </div>
</article>

<article class="auction alt" style="top:810px">
  <div class="photo" role="img" aria-label="Photo of a two-storey house with a garage"></div>
  <div class="btn details"><svg width="12" height="12" viewBox="0 0 12 12"><circle cx="5" cy="5" r="3.5" fill="none" stroke="#fff" stroke-width="1.6"/><path d="M7.6 7.6 11 11" stroke="#fff" stroke-width="1.8"/></svg><span>Details</span></div>
  <div class="btn gallery"><svg width="14" height="12" viewBox="0 0 14 12"><rect x="1" y="1" width="9" height="7" fill="none" stroke="#fff" stroke-width="1.4"/><rect x="4" y="4" width="9" height="7" fill="#0b4d12" stroke="#fff" stroke-width="1.4"/></svg><span>Gallery</span></div>
  <div class="card" style="top:10px;height:66px">
    <div class="h" style="top:9px">Auction 1</div>
    <div class="s" style="top:28px">Lorem Ipsum is simply dummy text of the printing and typesetting industry.</div>
  </div>
  <div class="card" style="top:89px;height:100px">
    <div class="h" style="top:7px">Online Bidding Only</div>
    <div class="s" style="top:23px">Began:&nbsp; Friday, May 24, 2013 at 10:06 AM EDT</div>
    <div class="s" style="top:43px"><b>Location</b><br>1720 Birch Ln. NW Ridgeview, IA 52400</div>
    <div class="s" style="top:69px;font-size:9.6px">Field tractor w/Hartline Loader, Dune Cutditioner: SHOP &amp; MISCELLANIOUS &amp; PORK .</div>
  </div>
</article>

<footer class="footer">
  <address>
    HALLEK Real Estate &amp; Auction Company LLC<br>
    Dale Hallek<br>
    418 Mill Street, P.O. Box 271<br>
    Fairmont, IL 62400<br>
    Phone 618-555-0142 or 1-800-555-0199<br>
    dale@hallekauctions.com
  </address>
  <div class="wordmark footer-mark"><span class="mark"></span>Hallek</div>
</footer>
<div class="copyright">Copyright © 2014 Hallek Real Estate All Rights Reserved.</div>

</body>
</html>
```